Post card selling a software for elderly visitor security

I need a postcard re-design that will entice children of elderly parents to sign-up to monitor the visitors (via online reporting dashboard) that care for them. These elderly residents live in a nursing home and many can't remember who came in the room to care for them. This is a major safety and security issue and adult children sometimes have no way of knowing who is visiting their parents. Our software provides an online reporting dashboard and sends text messages to adult children when a visitor arrives at the nursing home.

Target Market(s)

women between 50-65

Industry/Entity Type

Nursing Home

Colors

Designer to choose colors to be used in the design.

Requirements
Must have
• Must have Two questions: Are you the Primary Guardian of a resident in this community? If so, would you like to know who is visiting them?
• Must have a desktop computer and phone
• Needs to have a white background

```html
<!DOCTYPE html>
<html lang="en">
<head>
<meta charset="utf-8">
<title>Keepwell Visitor Postcard</title>
<link rel="stylesheet" href="https://fonts.googleapis.com/css2?family=Lato:ital,wght@0,400;0,700;0,900;1,400&display=swap">
<style>
  :root{
    --paper:#ffffff;
    --ink:#3a3a3a;
    --brand-blue:#1f6fb8;
    --screen-top:#1c5fa8;
    --screen-bottom:#3fa6e0;
    --bezel:#1d1d1f;
    --stand:#c9ccd0;
    --chin:#d9dbde;
    --offer-teal:#3f6f7d;
    --offer-cream:#f3efe3;
    --offer-gold:#c98f22;
    --bubble-red:#e2575c;
    --bubble-navy:#254a75;
    --ui-line:#d7dbe0;
    --ui-text:#5a6270;
    --photo:#9fc3d8;
  }
  *{margin:0;padding:0;box-sizing:border-box}
  html,body{width:1200px;height:765px;overflow:hidden;background:var(--paper)}
  .postcard{position:relative;width:1200px;height:765px;background:var(--paper);font-family:"Lato",sans-serif;color:var(--ink)}
  .headline{position:absolute;left:0;right:0;top:48px;text-align:center}
  .headline__question{font-size:30px;font-weight:400;letter-spacing:-.2px}
  .headline__question strong{color:var(--brand-blue);font-weight:700}
  .headline__follow-up{font-size:26px;font-style:italic;margin-top:6px}
  .desktop{position:absolute;left:150px;top:150px;width:720px;height:590px}
  .phone{position:absolute;left:800px;top:380px;width:170px;height:350px}
  .bubble{position:absolute;width:120px;height:78px;border-radius:14px;color:#fff;font-size:15px;line-height:1.15;display:flex;align-items:center;justify-content:center;text-align:center;padding:8px;border:3px solid #fff;box-shadow:0 2px 6px rgba(0,0,0,.2)}
  .bubble--arrival{background:var(--bubble-red);left:935px;top:440px}
  .bubble--departure{background:var(--bubble-navy);left:945px;top:545px}
  .bubble::after{content:"";position:absolute;left:14px;bottom:-14px;border:8px solid transparent;border-top:10px solid #fff}
  .trial-offer{position:absolute;left:830px;top:176px;width:180px;height:180px;border-radius:50%;background:var(--offer-cream);border:12px solid var(--offer-teal);display:flex;flex-direction:column;align-items:center;justify-content:center;text-align:center;line-height:1.05}
  .trial-offer__days{font-size:28px;font-weight:900;color:var(--ink);letter-spacing:.5px}
  .trial-offer__title{font-size:26px;font-weight:700;color:var(--offer-gold);margin:4px 0}
  .trial-offer__risk{font-size:15px;font-weight:700;color:var(--ink);letter-spacing:1px}
  .ui-text{font-family:"Lato",sans-serif;fill:var(--ui-text)}
</style>
</head>
<body>
<main class="postcard">
  <header class="headline">
    <h1 class="headline__question">Are you the <strong>Primary Guardian</strong> of a resident in this community?</h1>
    <p class="headline__follow-up">If so, would you like to know who is visiting them?</p>
  </header>

  <svg class="desktop" viewBox="0 0 720 590" aria-label="Desktop computer showing the visitor dashboard">
    <defs>
      <linearGradient id="screen-glow" x1="0" y1="0" x2="0" y2="1">
        <stop offset="0" stop-color="var(--screen-top)"/><stop offset="1" stop-color="var(--screen-bottom)"/>
      </linearGradient>
    </defs>
    <rect class="desktop__bezel" x="0" y="0" width="720" height="430" rx="14" fill="var(--bezel)"/>
    <rect class="desktop__screen" x="18" y="18" width="684" height="394" fill="url(#screen-glow)"/>
    <rect class="desktop__chin" x="0" y="420" width="720" height="70" rx="10" fill="var(--chin)"/>
    <path class="desktop__stand" d="M300 490 L420 490 L440 570 L280 570 Z" fill="var(--stand)"/>
    <rect x="260" y="568" width="200" height="10" rx="4" fill="#b8bbbf"/>

    <g class="dashboard">
      <rect x="70" y="40" width="580" height="300" fill="#fff"/>
      <rect x="70" y="40" width="580" height="16" fill="#eceef1"/>
      <rect x="70" y="56" width="18" height="284" fill="#2e3a48"/>
      <text class="ui-text" x="100" y="80" font-size="15" fill="#444">Keepwell Visitor Dashboard</text>
      <text class="ui-text" x="100" y="93" font-size="8">for XYZ Senior Living</text>
      <text class="ui-text" x="100" y="115" font-size="8">Search for Events</text>
      <text class="ui-text" x="100" y="128" font-size="6">Starting</text>
      <text class="ui-text" x="160" y="128" font-size="6">Ending</text>
      <text class="ui-text" x="220" y="128" font-size="6">Search By</text>
      <rect x="100" y="132" width="50" height="10" fill="none" stroke="var(--ui-line)"/>
      <rect x="160" y="132" width="50" height="10" fill="none" stroke="var(--ui-line)"/>
      <rect x="220" y="132" width="50" height="10" fill="none" stroke="var(--ui-line)"/>
      <rect x="290" y="132" width="30" height="10" fill="var(--brand-blue)"/>
      <text x="295" y="140" font-size="6" fill="#fff" font-family="Lato,sans-serif">Submit</text>
      <circle cx="555" cy="100" r="18" fill="#4a90d9"/>
      <path d="M555 100 L555 82 A18 18 0 0 1 572 106 Z" fill="#7ac36a"/>
      <circle cx="600" cy="100" r="18" fill="#d94f8a"/>
      <circle cx="600" cy="100" r="9" fill="#fff"/>
      <text class="ui-text" x="100" y="165" font-size="11">Export Visits</text>
      <rect x="100" y="172" width="36" height="10" fill="var(--brand-blue)"/>
      <g class="ui-text" font-size="6">
        <text x="100" y="205">Date</text><text x="140" y="205">Sign In</text><text x="180" y="205">Sign Out</text>
        <text x="230" y="205">Resident</text><text x="280" y="205">Visitor</text><text x="330" y="205">Phone</text><text x="380" y="205">Company</text>
      </g>
      <rect x="96" y="212" width="330" height="22" fill="#fbf5d6"/>
      <g class="ui-text" font-size="6">
        <text x="100" y="226">12/30/18</text><text x="140" y="226">10:15</text><text x="180" y="226">11:02</text><text x="230" y="226">Moss</text><text x="280" y="226">Jones</text>
        <text x="100" y="256">12/29/18</text><text x="140" y="256">14:20</text><text x="180" y="256">15:05</text><text x="230" y="256">Moss</text><text x="280" y="256">Jones</text>
      </g>
      <line x1="96" y1="240" x2="426" y2="240" stroke="var(--ui-line)"/>
      <line x1="280" y1="230" x2="320" y2="290" stroke="#e23b3b" stroke-width="2"/>
      <rect x="600" y="205" width="40" height="14" fill="#fff" stroke="var(--ui-line)"/>
      <text x="606" y="215" font-size="7" fill="var(--brand-blue)" font-family="Lato,sans-serif">+ Visit</text>
    </g>

    <g class="visitor-photos">
      <rect x="310" y="270" width="380" height="150" fill="#fff" stroke="#2b6cb0" stroke-width="2"/>
      <text class="ui-text" x="320" y="288" font-size="11" fill="#444">Visitor Photos</text>
      <text class="ui-text" x="320" y="300" font-size="6">These are photos of Rita Moss taken during a sign in on 12/31/2018 at 11:01 PM</text>
      <rect role="img" aria-label="Visitor sign-in photo" x="335" y="308" width="120" height="105" fill="var(--photo)"/>
      <rect role="img" aria-label="Second visitor sign-in photo" x="475" y="308" width="120" height="105" fill="var(--photo)"/>
    </g>
  </svg>

  <aside class="trial-offer" aria-label="30-day free trial, no risk">
    <span class="trial-offer__days">30-DAY</span>
    <span class="trial-offer__title">Free Trial</span>
    <span class="trial-offer__risk">NO RISK!</span>
  </aside>

  <svg class="phone" viewBox="0 0 170 350" aria-label="Smartphone showing visitor text alerts">
    <defs>
      <linearGradient id="phone-glow" x1="0" y1="0" x2="0" y2="1">
        <stop offset="0" stop-color="#5a7fa8"/><stop offset=".55" stop-color="#d9546a"/><stop offset="1" stop-color="#2f6e7a"/>
      </linearGradient>
    </defs>
    <rect x="0" y="0" width="170" height="350" rx="26" fill="var(--bezel)"/>
    <rect x="8" y="8" width="154" height="334" rx="20" fill="url(#phone-glow)"/>
    <rect x="55" y="8" width="60" height="14" rx="7" fill="var(--bezel)"/>
    <text x="85" y="70" text-anchor="middle" font-size="36" fill="#fff" font-family="Lato,sans-serif">9:41</text>
    <text x="85" y="88" text-anchor="middle" font-size="9" fill="#fff" font-family="Lato,sans-serif">Monday, June 4</text>
    <rect x="16" y="110" width="138" height="52" rx="8" fill="rgba(255,255,255,.75)"/>
    <text x="24" y="124" font-size="7" fill="#333" font-family="Lato,sans-serif">MESSAGES</text>
    <text x="24" y="140" font-size="9" fill="#222" font-family="Lato,sans-serif">Dr. Jones has arrived</text>
    <rect x="16" y="170" width="138" height="52" rx="8" fill="rgba(255,255,255,.75)"/>
    <text x="24" y="184" font-size="7" fill="#333" font-family="Lato,sans-serif">VISITOR ALERT</text>
    <text x="24" y="200" font-size="9" fill="#222" font-family="Lato,sans-serif">Dad signed out at 4:12 PM</text>
  </svg>

  <div class="bubble bubble--arrival">Dr. Jones arrived to see Mom</div>
  <div class="bubble bubble--departure">Dad left the community</div>
</main>
</body>
</html>
```